Billboard design - consider what a billboard is

Design a billboard using my logo - Billboard is 6m x 3m
A Billboard is advertising for my company that is on a big sign.

Has to be clean and easy to read, and ideally highlights that we are Residential and Commercial builders.

Keep it clean and easy to read

The contact number for the board is

022 583 7092
www.harbourframeworks.co.nz
info@harbourframeworks.co.nz

Doesnt have to have all contact details if it doesnt fit

Has to catch peoples attention to contact us if they need a builder

Can you please change the sign to be all white writing, with black background ?
Updates

Please consider what a billboard is...

The design needs to be suitable for a billboard..

Target Market(s)

people driving past

Industry/Entity Type

Construction

Logo Text

Wellington Builder, website email address, contact number

Colors
0054AA
0677BA
7BADD7
CADEEF
E8F1F8

Requirements
Must have
• Easy to read
Nice to have
• easy to read, can clearly see contact details

```html
<!DOCTYPE html>
<html lang="en">
<head>
<meta charset="utf-8">
<title>Harbour Frameworks Billboard</title>
<link rel="stylesheet" href="https://fonts.googleapis.com/css2?family=Crimson+Pro:wght@700&display=swap">
<style>
  :root {
    --ink: #FFFFFF;
    --mid-blue: #5B8FCF;
    --pale-blue: #C8DFF0;
    --board: #000000;
    --edge: #333333;
  }
  html, body {
    margin: 0;
    padding: 0;
    overflow: hidden;
    background: var(--board);
  }
  .billboard {
    position: relative;
    width: 1200px;
    height: 601px;
    background: var(--board);
    box-sizing: border-box;
    border: 1px solid var(--edge);
    overflow: hidden;
    font-family: "Crimson Pro", "Palatino Linotype", Georgia, serif;
    font-weight: 700;
    color: var(--ink);
  }
  .imagery {
    position: absolute;
    left: 0;
    top: 0;
    width: 1200px;
    height: 601px;
  }
  .brand {
    position: absolute;
    top: 52px;
    right: 36px;
    display: flex;
    align-items: center;
    gap: 10px;
  }
  .brand-square {
    width: 18px;
    height: 18px;
    background: var(--ink);
  }
  .brand-name {
    font-size: 36px;
    line-height: 1;
    letter-spacing: 0.2px;
  }
  .services {
    position: absolute;
    left: 36px;
    top: 250px;
    margin: 0;
    font-size: 40px;
    line-height: 1.1;
  }
  .contact {
    position: absolute;
    left: 36px;
    top: 345px;
  }
  .contact-phone {
    margin: 0;
    font-size: 116px;
    line-height: 1;
    letter-spacing: 1px;
  }
  .contact-line {
    margin: 0;
    font-size: 44px;
    line-height: 42px;
  }
  .contact-web { margin-top: 10px; }
</style>
</head>
<body>
  <div class="billboard">
    <svg class="imagery" viewBox="0 0 1200 601" xmlns="http://www.w3.org/2000/svg">
      <defs>
        <linearGradient id="towerGlass" x1="0" y1="0" x2="1" y2="1">
          <stop offset="0" stop-color="#FFFFFF"/>
          <stop offset="0.35" stop-color="#9CC0E2"/>
          <stop offset="1" stop-color="#3D6E9E"/>
        </linearGradient>
        <linearGradient id="apartmentFacade" x1="0" y1="0" x2="1" y2="1">
          <stop offset="0" stop-color="#3F7FE0"/>
          <stop offset="0.45" stop-color="#C9B89A"/>
          <stop offset="1" stop-color="#E8D7B8"/>
        </linearGradient>
      </defs>
      <polygon class="accent-pale" fill="var(--pale-blue)" points="616,0 628,0 628,248 866,486 853,490 616,253"/>
      <polygon class="photo-tower" fill="url(#towerGlass)" role="img"
               aria-label="Photo of a glass-clad commercial tower seen from below"
               points="628,0 866,0 866,490 628,252"/>
      <polygon class="accent-mid" fill="var(--mid-blue)" points="878,111 1117,350 1117,601 866,601 866,111"/>
      <polygon class="photo-apartments" fill="url(#apartmentFacade)" role="img"
               aria-label="Photo of a residential apartment block with glass balconies against a blue sky"
               points="866,111 1104,349 1104,601 866,601"/>
    </svg>

    <div class="brand">
      <span class="brand-square"></span>
      <span class="brand-name">Harbour Frameworks</span>
    </div>

    <p class="services">Residential &amp; Commercial Builders</p>

    <div class="contact">
      <p class="contact-phone">022 583 7092</p>
      <p class="contact-line contact-web">www.harbourframeworks.co.nz</p>
      <p class="contact-line contact-email">info@harbourframeworks.co.nz</p>
    </div>
  </div>
</body>
</html>
```